■依頼詳細

<デザインのサイズ> ヨコ 300mm x タテ 230mm
<入稿データ> Ai形式(CMYKカラー)

ラミジップ袋そのものに印刷をするか、
あるいは、袋の中に印刷した型紙を封入するかは
まだ決まっておりません。

裏面はありません。
表面(一面)のみのデザインでお願いします。

■ブランド名とロゴについて

ブランド名、および入れたいテキスト内容は
添付のファイルを参照してください。

ブランドロゴがまだ決まっておりませんので、
パッケージに合わせてロゴの制作もお願いします。

■商品のターゲット層

20代~30代の女性が買っています。
ヘアケア用品なので、美容に意識の高い方になります。

■デザインの希望

とにかく可愛く、オシャレなデザインが希望です。
シルク100%なので、高級感もあると良いです。

商品は全部で15色のカラバリがあります。
なので、パッケージの色に希望はありません。
カラフルでも、単色でも、グラデーションでも良いです。

暗い色合いやデザインはNGです。
明るいデザインでお願いします。

通販サイトのサムネイル画像になっても視認性が落ちない、
パッと見てこの商品だとわかるデザインだととても良いです。

■参考になる他社
https://www.merolto.co.jp/dp/Q72KM4ZTRP/ref=cm_sw_r_tw_dp_x_4LT2WdRNB7PQJ
こちらのブランドは高級感がウリです。
弊社は「可愛い」「オシャレ」がウリになります。
ブランド名をメインにデザインしてください。
(※ブランド名は添付のファイルを参照してください)

■その他のテキスト内容
(下記テキストの挿入は必須ではありません。無くても良いです)

「Silk100%」「シルク100%」
「Night Cap」「ナイトキャップ」
「Silk Night Cap」「シルクナイトキャップ」

英字の文章などを適当に入れていただくこともOKです。

ご提案を見て、一番最初に目が行き、美しい!と感じたデザインでした。
ご依頼内容をよく理解されていて、こちらの意図がよく汲まれたレイアウトや配色だったことも理由です。

たくさんのご応募、誠にありがとうございます。
依頼内容をしっかりと汲んでいただいたご提案が多く、選定にとても悩みました。
そのくらい良いデザインが多かったです。ありがとうございます。
また機会がございましたら、何卒よろしくお願い申し上げます。

```html
<!DOCTYPE html>
<html lang="ja">
<head>
<meta charset="utf-8">
<title>NOVASILK Silk Night Cap – Package Colour Variations</title>
<link href="https://fonts.googleapis.com/css2?family=Zen+Maru+Gothic:wght@500;700&family=Noto+Serif+JP:wght@500&display=swap" rel="stylesheet">
<style>
  :root {
    --backdrop: #f7d5d8;
    --bag: #fbfbfc;
    --bag-edge: #e4e4e8;
    --ink: #ffffff;
    --label: #333333;
    --blue-a: #3f7fd0; --blue-b: #a9cdf0;
    --pink-a: #e0526f; --pink-b: #f6c2cc;
    --purple-a: #6e579e; --purple-b: #c2b3dc;
    --green-a: #2f8255; --green-b: #b3d8c2;
  }
  * { margin: 0; padding: 0; box-sizing: border-box; }
  html, body { width: 1200px; height: 977px; overflow: hidden; }
  body {
    background: var(--backdrop);
    position: relative;
    font-family: "Zen Maru Gothic", sans-serif;
  }
  .sheet-mark {
    position: absolute; left: 1155px; top: 22px;
    font-size: 22px; color: var(--label);
  }
  .bag {
    position: absolute; width: 496px; height: 376px;
    background: var(--bag);
    border-radius: 6px;
    box-shadow: 0 2px 8px rgba(120, 80, 90, .25);
    overflow: hidden;
  }
  .bag--blue   { left: 90px;  top: 94px;  --a: var(--blue-a);   --b: var(--blue-b); }
  .bag--pink   { left: 630px; top: 94px;  --a: var(--pink-a);   --b: var(--pink-b); }
  .bag--purple { left: 90px;  top: 504px; --a: var(--purple-a); --b: var(--purple-b); }
  .bag--green  { left: 630px; top: 504px; --a: var(--green-a);  --b: var(--green-b); }
  .zip {
    position: absolute; left: 0; right: 0; top: 30px; height: 12px;
    border-top: 1px solid var(--bag-edge);
    border-bottom: 1px solid var(--bag-edge);
  }
  .window {
    position: absolute; left: 36px; top: 60px; width: 426px; height: 288px;
    border-radius: 22px;
    background:
      linear-gradient(125deg, var(--b) 0%, var(--a) 30%, var(--b) 52%, var(--a) 72%, var(--b) 100%);
    filter: blur(7px);
    opacity: .9;
  }
  .copy {
    position: absolute; left: 0; top: 0; width: 100%; height: 100%;
    color: var(--ink); text-align: center;
  }
  .copy > * { position: absolute; left: 0; right: 0; }
  .lead { top: 84px; font-size: 18px; font-weight: 700; letter-spacing: 1px; }
  .brand {
    top: 146px; font-size: 50px; font-weight: 700; letter-spacing: 2px; line-height: 1;
  }
  .product-en {
    top: 210px; font-family: "Noto Serif JP", serif; font-size: 19px; letter-spacing: 1px;
  }
  .product-ja { top: 254px; font-size: 15px; font-weight: 700; letter-spacing: 1px; }
  .tagline { top: 279px; font-size: 16px; font-weight: 700; letter-spacing: 1px; }
  .silk-badge {
    left: 378px !important; right: auto !important; top: 214px;
    width: 52px; height: 52px; border-radius: 50%;
    background: var(--ink); color: var(--a);
    font-family: "Noto Serif JP", serif; font-size: 12px; line-height: 1.15;
    display: flex; flex-direction: column; justify-content: center; align-items: center;
  }
  .legend {
    position: absolute; left: 96px; top: 920px;
    display: flex; align-items: center; gap: 8px;
    font-size: 22px; color: var(--label);
  }
  .legend-swatch { width: 28px; height: 28px; background: var(--ink); }
</style>
</head>
<body>
  <div class="sheet-mark">A</div>

  <div class="bag bag--blue">
    <div class="zip"></div>
    <div class="window" role="img" aria-label="Blurred photo of a blue silk night cap behind a star pattern"></div>
    <div class="copy">
      <p class="lead">髪にうるおいを</p>
      <p class="brand">NOVASILK</p>
      <p class="product-en">Silk Night Cap</p>
      <p class="silk-badge"><span>Silk</span><span>100%</span></p>
      <p class="product-ja">シルクナイトキャップ</p>
      <p class="tagline">寝ている間にしっとりツヤツヤ</p>
    </div>
  </div>

  <div class="bag bag--pink">
    <div class="zip"></div>
    <div class="window" role="img" aria-label="Blurred photo of a pink silk night cap behind a star pattern"></div>
    <div class="copy">
      <p class="lead">髪にうるおいを</p>
      <p class="brand">NOVASILK</p>
      <p class="product-en">Silk Night Cap</p>
      <p class="silk-badge"><span>Silk</span><span>100%</span></p>
      <p class="product-ja">シルクナイトキャップ</p>
      <p class="tagline">寝ている間にしっとりツヤツヤ</p>
    </div>
  </div>

  <div class="bag bag--purple">
    <div class="zip"></div>
    <div class="window" role="img" aria-label="Blurred photo of a purple silk night cap behind a star pattern"></div>
    <div class="copy">
      <p class="lead">髪にうるおいを</p>
      <p class="brand">NOVASILK</p>
      <p class="product-en">Silk Night Cap</p>
      <p class="silk-badge"><span>Silk</span><span>100%</span></p>
      <p class="product-ja">シルクナイトキャップ</p>
      <p class="tagline">寝ている間にしっとりツヤツヤ</p>
    </div>
  </div>

  <div class="bag bag--green">
    <div class="zip"></div>
    <div class="window" role="img" aria-label="Blurred photo of a green silk night cap behind a star pattern"></div>
    <div class="copy">
      <p class="lead">髪にうるおいを</p>
      <p class="brand">NOVASILK</p>
      <p class="product-en">Silk Night Cap</p>
      <p class="silk-badge"><span>Silk</span><span>100%</span></p>
      <p class="product-ja">シルクナイトキャップ</p>
      <p class="tagline">寝ている間にしっとりツヤツヤ</p>
    </div>
  </div>

  <div class="legend"><span class="legend-swatch"></span><span>使用色：1色</span></div>
</body>
</html>
```